Deactivated Coal-Fired Power Plant to be redeveloped into a Green Energy Campus.

Want a striking business card statement that introduces our concept project to provide economic and community recovery to a former rural coal community in western PA.
Essentially 12 project representatives that will lead both the demolition of an existing power plant and the redevelopment to a new Green energy site.
Business Card should reflect our effort.
We are open to ideas.

Target Market(s)

Energy and Power Generation industries

Industry/Entity Type

Power Generation and Data Centers

Contact Information for Business Card

Included in uploaded materials

Font styles to use
Sans Serif
Other font styles liked:
• Arial, Calibri

Requirements
Must have
• Multiple colors

```html
<!DOCTYPE html>
<html lang="en">
<head>
<meta charset="utf-8">
<title>Ridgeline Renewal – Business Card</title>
<link href="https://fonts.googleapis.com/css2?family=Outfit:wght@400;600;700&display=swap" rel="stylesheet">
<style>
  :root {
    --page-bg: #e4e2e4;
    --card-bg: #eeeeef;
    --brand-green: #1d9a48;
    --ink: #161616;
    --muted-grey: #c9cbcd;
    --sky-blue: #a9c2cf;
    --field-green: #8fb36a;
  }
  * { box-sizing: border-box; margin: 0; padding: 0; }
  html, body {
    width: 1200px; height: 900px; overflow: hidden;
    background: var(--page-bg);
    font-family: "Outfit", Arial, sans-serif;
    color: var(--ink);
  }
  .stage {
    position: relative; width: 1200px; height: 900px;
  }
  .card {
    position: absolute; left: 290px; width: 620px; height: 354px;
    background: var(--card-bg);
    overflow: hidden;
  }
  .card--front { top: 80px; }
  .card--back { top: 466px; }

  /* Front */
  .front-scene {
    position: absolute; inset: 0;
    background:
      radial-gradient(ellipse 38% 55% at 50% 55%, rgba(255,255,255,0.95), rgba(255,255,255,0) 70%),
      linear-gradient(90deg, #9a9c9e 0%, #c4c6c7 30%, #f2f2f2 50%, var(--sky-blue) 68%, #b9cdb0 82%, var(--field-green) 100%);
  }
  .front-mark {
    position: absolute; left: 0; right: 0; top: 200px;
    display: flex; align-items: center; justify-content: center; gap: 14px;
  }
  .brand-dot {
    width: 34px; height: 34px; border-radius: 50%;
    background: var(--brand-green);
  }
  .brand-name {
    font-weight: 700; color: var(--ink); letter-spacing: 0.5px;
    text-transform: uppercase; line-height: 1;
  }
  .front-mark .brand-name { font-size: 40px; }

  /* Back */
  .back-mark {
    position: absolute; left: 0; right: 0; top: 96px;
    display: flex; align-items: center; justify-content: center; gap: 10px;
  }
  .back-mark .brand-dot { width: 22px; height: 22px; }
  .back-mark .brand-name { font-size: 25px; }
  .divider {
    position: absolute; left: 53px; right: 53px; top: 184px;
    height: 2px; background: var(--brand-green);
  }
  .person {
    position: absolute; left: 53px; top: 230px;
  }
  .person-name { font-size: 24px; font-weight: 700; letter-spacing: -0.3px; margin-bottom: 8px; }
  .person-role, .person-company { font-size: 16px; color: var(--brand-green); line-height: 1.45; }
  .contacts {
    position: absolute; left: 390px; top: 234px;
    list-style: none;
  }
  .contact {
    display: flex; align-items: center; gap: 11px;
    font-size: 16px; height: 28px;
  }
  .contact-icon {
    width: 20px; height: 20px; border-radius: 50%;
    background: var(--brand-green);
    display: flex; align-items: center; justify-content: center;
  }
</style>
</head>
<body>
<main class="stage">
  <section class="card card--front">
    <div class="front-scene" role="img" aria-label="Photo blend of an old coal power plant with smokestacks fading into wind turbines, green fields and solar panels"></div>
    <div class="front-mark">
      <span class="brand-dot"></span>
      <span class="brand-name">Ridgeline Renewal</span>
    </div>
  </section>

  <section class="card card--back">
    <div class="back-mark">
      <span class="brand-dot"></span>
      <span class="brand-name">Ridgeline Renewal</span>
    </div>
    <div class="divider"></div>
    <div class="person">
      <p class="person-name">Daniel Hartwell</p>
      <p class="person-role">Chief Operating Officer</p>
      <p class="person-company">Ridgeline Renewal LLC.</p>
    </div>
    <ul class="contacts">
      <li class="contact">
        <span class="contact-icon">
          <svg width="12" height="12" viewBox="0 0 12 12" fill="none" stroke="#fff" stroke-width="1.3"><rect x="1" y="2.5" width="10" height="7" rx="1"/><path d="M1.5 3l4.5 3.5L10.5 3"/></svg>
        </span>
        <span>dhartwell@example.com</span>
      </li>
      <li class="contact">
        <span class="contact-icon">
          <svg width="12" height="12" viewBox="0 0 12 12"><path fill="#fff" d="M3 1.2l1.6 2.2-.9 1.2a6 6 0 0 0 3.7 3.7l1.2-.9 2.2 1.6-.9 1.8C6 10.6 1.4 6 1.2 2.1z"/></svg>
        </span>
        <span>555-201-334</span>
      </li>
      <li class="contact">
        <span class="contact-icon">
          <svg width="12" height="12" viewBox="0 0 12 12" fill="none" stroke="#fff" stroke-width="1.3"><rect x="3.2" y="1" width="5.6" height="10" rx="1"/><path d="M5.3 9h1.4"/></svg>
        </span>
        <span>555-708-912</span>
      </li>
    </ul>
  </section>
</main>
</body>
</html>
```